Bramble Travel Planners needs an bold logo and business card design

Thanks you all for helping me with this project your assistance is appriciated
I am starting a home based travel agency and I need a bold and eye catching logo and business card designed.
I want to convey a sense of FREEDOM, expertise, customer service for travel customers
Bramble travel planners is a full service travel agency focused on customer service and adding value to a vacation and travel planning.
my idea is for a card that looks like an cruise ship boarding pass or passport with stamps with a back drop of beautiful beach scene, resort hotel and happiness.
The logo should be eye catching, unique but give a sense of freedom and it should be travel related
We want to give customers a sense of Freedom from travel planning, freedom from researching cruises and hotels and freedom to enjoy a wonderful cost effective vacation.

Target Market(s)

Customers considering travel for vacations, family reunions, business and weddings

Industry/Entity Type

Travel Industry

Contact Information for Business Card

Bramble Travel Planners
Warren Pelfrey Owner
WPelfrey@BrambleTravelPlanners.com
BrambleTravelPlanners.com
(555) 014-2287

Logo Text

“One’s destination is never a place, but a new way of seeing things.”

Font styles to use
Serif

Colors
85cae6
0492cd
ec1f27
e667a6
b768aa
33b8a4

Requirements
Must have
• The Logo you create should be on the busoness card
• should be clean, easy to read and attractive
• something you that would make you want to work with a travel agent
Nice to have
• should have cruise ship, hotel on the card or something that conveys travel
Should not have
• Should not have the american flag
• no yellow on the card

```html
<!DOCTYPE html>
<html lang="en">
<head>
<meta charset="utf-8">
<title>Bramble Travel Planners – Business Card</title>
<link rel="stylesheet" href="https://fonts.googleapis.com/css2?family=Source+Sans+3:wght@400;600;700&display=swap">
<style>
  :root {
    --stage-top: #2b2b2b;
    --stage-bottom: #050505;
    --paper: #ffffff;
    --teal: #33b8a4;
    --teal-soft: #e8f6f3;
    --pink: #e667a6;
    --pink-soft: #fbeaf3;
    --ink: #1f1f1f;
  }
  * { margin: 0; padding: 0; box-sizing: border-box; }
  html, body { width: 1200px; height: 900px; overflow: hidden; }
  body {
    background: linear-gradient(180deg, var(--stage-top) 0%, #181818 45%, var(--stage-bottom) 100%);
    font-family: "Source Sans 3", Arial, sans-serif;
    position: relative;
  }
  .card {
    position: absolute;
    top: 306px;
    width: 440px;
    height: 271px;
    border-radius: 10px;
    overflow: hidden;
    box-shadow: 0 2px 6px rgba(0,0,0,0.45);
  }
  .card--front { left: 149px; background: var(--paper); }
  .card--back { left: 608px; background: var(--teal); }

  .front-wash {
    position: absolute;
    left: -60px; bottom: -70px;
    width: 360px; height: 170px;
    border-radius: 50%;
    background: radial-gradient(ellipse at center, var(--teal-soft) 0%, rgba(232,246,243,0) 70%);
  }
  .front-glow {
    position: absolute;
    left: 120px; top: 10px;
    width: 300px; height: 120px;
    border-radius: 50%;
    background: radial-gradient(ellipse at center, var(--pink-soft) 0%, rgba(251,234,243,0) 70%);
  }

  .contact-block {
    position: absolute;
    top: 22px;
    right: 25px;
    text-align: right;
  }
  .person-name { color: var(--teal); font-size: 16px; font-weight: 600; line-height: 18px; }
  .person-role { color: var(--pink); font-size: 14px; line-height: 17px; }
  .contact-list { list-style: none; margin-top: 19px; }
  .contact-item {
    display: flex; justify-content: flex-end; align-items: center; gap: 7px;
    color: var(--ink); font-size: 13px; line-height: 16px;
  }
  .contact-icon { width: 9px; height: 9px; fill: var(--teal); flex: none; }

  .brand {
    position: absolute;
    display: flex;
    align-items: center;
  }
  .brand-dot { border-radius: 50%; background: var(--pink); flex: none; }
  .brand-name {
    color: var(--pink);
    font-weight: 700;
    white-space: nowrap;
    display: flex;
    flex-direction: column;
    align-items: flex-end;
    line-height: 1;
  }
  .brand-sub { display: block; }

  .card--front .brand { left: 22px; top: 200px; gap: 8px; }
  .card--front .brand-dot { width: 20px; height: 20px; }
  .card--front .brand-main { font-size: 25px; }
  .card--front .brand-sub { font-size: 13px; margin-top: 1px; }

  .card--back .brand { left: 76px; top: 118px; gap: 12px; }
  .card--back .brand-dot { width: 34px; height: 34px; }
  .card--back .brand-main { font-size: 41px; }
  .card--back .brand-sub { font-size: 18px; margin-top: 0; }
</style>
</head>
<body>
  <section class="card card--front" aria-label="Business card front">
    <div class="front-glow" aria-hidden="true"></div>
    <div class="front-wash" aria-hidden="true"></div>
    <div class="contact-block">
      <p class="person-name">Warren Pelfrey</p>
      <p class="person-role">Owner</p>
      <ul class="contact-list">
        <li class="contact-item">(555) 014-2287
          <svg class="contact-icon" viewBox="0 0 10 10" aria-hidden="true"><path d="M1 3.5C1 2 2.5 1 5 1s4 1 4 2.5L7.5 4.3 6.8 3H3.2L2.5 4.3zM2.5 5h5L9 8.5H1z"/></svg>
        </li>
        <li class="contact-item">WPelfrey@BrambleTravelPlanners.com
          <svg class="contact-icon" viewBox="0 0 10 10" aria-hidden="true"><path d="M0.5 2h9v6h-9z"/><path d="M0.5 2l4.5 3.5L9.5 2" fill="none" stroke="#fff" stroke-width="0.9"/></svg>
        </li>
        <li class="contact-item">www.BrambleTravelPlanners.com
          <svg class="contact-icon" viewBox="0 0 10 10" aria-hidden="true"><path d="M6 1.5l2.5 2.5-4.5 4.5L1.5 6z" fill="none" stroke="#33b8a4" stroke-width="1.2"/></svg>
        </li>
      </ul>
    </div>
    <div class="brand">
      <span class="brand-dot" aria-hidden="true"></span>
      <p class="brand-name"><span class="brand-main">Bramble Travel</span><span class="brand-sub">Planners</span></p>
    </div>
  </section>

  <section class="card card--back" aria-label="Business card back">
    <div class="brand">
      <span class="brand-dot" aria-hidden="true"></span>
      <p class="brand-name"><span class="brand-main">Bramble Travel</span><span class="brand-sub">Planners</span></p>
    </div>
  </section>
</body>
</html>
```